Brenvik Auto Logo Design

Brenvik Auto Sales & Service is a automotive repair shop and car dealership. We specialize in Norvane & Kestrelwerk, so we would like our cards to let our customers know that we are a German import specialist and that we are QTR certified. We are looking for something that is sharp, with clean lines, and very professional. We specialize in Norvane and Kestrelwerk, so we want to appeal to the higher end customer. We want a business card that will do so. Please no cars, tires or tools on the logo. We want this to look tactful and professional. We would also like our link to our facebook page included on the business card. https://www.examplesocial.test/brenvikautosalesservice

Industry/Entity Type

Automotive

Contact Information for Business Card

Brenvik Auto Sales & Service
Doug & Melinda Brenvik
482 E Thornbury Avenue
PO Box 63
Dellhaven, MN 54911
Phone 715-555-0187
Fax 715-555-0193

Logo Text

```html
<!DOCTYPE html>
<html lang="en">
<head>
<meta charset="utf-8">
<title>Brenvik Auto Sales &amp; Service – Business Card</title>
<link href="https://fonts.googleapis.com/css2?family=Michroma&family=Exo+2:wght@400&display=swap" rel="stylesheet">
<style>
  :root {
    --page: #ffffff;
    --card-dark: #0b0b0c;
    --card-dark-edge: #1c1d1f;
    --steel-blue: #4a7d98;
    --steel-blue-deep: #3d6f8b;
    --silver-light: #f2f2f2;
    --silver-mid: #c9c9c9;
    --silver-dark: #a9a9a9;
    --ink-grey: #4a4a4a;
    --text-light: #c8c8c8;
    --rule: #8a8a8a;
  }
  * { box-sizing: border-box; margin: 0; padding: 0; }
  html, body {
    width: 1200px; height: 800px; overflow: hidden;
    background: var(--page);
  }
  .canvas { position: relative; width: 1200px; height: 800px; }

  .card {
    position: absolute;
    width: 525px; height: 300px;
    overflow: hidden;
    box-shadow: 0 6px 18px rgba(0,0,0,.25);
  }

  /* ---------- Contact side (dark) ---------- */
  .card--contact {
    left: 50px; top: 230px;
    background: radial-gradient(circle at 55% 40%, var(--card-dark-edge) 0%, var(--card-dark) 70%);
  }
  .card--contact .accent-stripe {
    position: absolute; left: 0; right: 0; bottom: 22px;
    height: 4px; background: var(--steel-blue);
  }
  .card--contact .brand {
    position: absolute; left: 40px; top: 34px;
    display: flex; align-items: center; gap: 14px;
  }
  .brand-dot {
    width: 54px; height: 54px; border-radius: 50%;
    background: var(--steel-blue);
    flex: none;
  }
  .brand-name {
    font-family: "Michroma", sans-serif;
    font-size: 18px; letter-spacing: 2px;
    color: var(--silver-mid);
    white-space: nowrap;
  }
  .card--contact .tagline {
    position: absolute; left: 40px; top: 104px;
    font-family: "Michroma", sans-serif;
    font-size: 10px; letter-spacing: 1.5px;
    color: var(--text-light);
  }
  .card--contact .divider {
    position: absolute; left: 40px; right: 40px; top: 136px;
    height: 1px; background: var(--rule);
  }
  .card--contact .owners {
    position: absolute; left: 40px; top: 156px;
    font-family: "Michroma", sans-serif;
    font-size: 13px; letter-spacing: 2.5px;
    color: var(--text-light);
  }
  .contact-list {
    position: absolute; left: 40px; top: 190px;
    list-style: none;
    font-family: "Exo 2", sans-serif;
    font-size: 13px; letter-spacing: .5px;
    color: var(--text-light);
  }
  .contact-list li { display: flex; align-items: center; gap: 8px; margin-bottom: 8px; white-space: nowrap; }
  .contact-list svg { width: 11px; height: 11px; flex: none; }

  /* ---------- Logo side (silver) ---------- */
  .card--logo {
    left: 625px; top: 40px;
    background: radial-gradient(circle at 62% 45%, var(--silver-light) 0%, var(--silver-mid) 65%, var(--silver-dark) 100%);
  }
  .card--logo .corner-swoosh {
    position: absolute; right: 0; bottom: 0; width: 200px; height: 150px;
  }
  .card--logo .brand {
    position: absolute; left: 190px; top: 60px;
    display: flex; align-items: center; gap: 18px;
  }
  .card--logo .brand-dot { width: 120px; height: 120px; }
  .card--logo .brand-name { font-size: 22px; color: var(--ink-grey); }
  .card--logo .tagline {
    position: absolute; left: 60px; top: 210px;
    font-family: "Michroma", sans-serif;
    font-size: 16px; letter-spacing: 3px;
    color: var(--ink-grey);
    white-space: nowrap;
  }

  /* ---------- Standalone logo lockup ---------- */
  .lockup {
    position: absolute; left: 815px; top: 540px; width: 360px;
    display: flex; flex-direction: column; align-items: center; gap: 22px;
  }
  .lockup .brand { display: flex; align-items: center; gap: 16px; }
  .lockup .brand-dot { width: 150px; height: 150px; }
  .lockup .brand-name { font-size: 20px; color: var(--ink-grey); }
  .lockup .tagline {
    font-family: "Michroma", sans-serif;
    font-size: 15px; letter-spacing: 2.5px;
    color: var(--ink-grey); white-space: nowrap;
  }
</style>
</head>
<body>
<main class="canvas">

  <section class="card card--contact" aria-label="Business card, contact side">
    <div class="brand">
      <span class="brand-dot" aria-hidden="true"></span>
      <span class="brand-name">BRENVIK</span>
    </div>
    <p class="tagline">AUTO SALES &amp; SERVICE</p>
    <div class="divider"></div>
    <p class="owners">DOUG &amp; MELINDA BRENVIK</p>
    <ul class="contact-list">
      <li>
        <svg viewBox="0 0 12 12" aria-hidden="true"><path d="M6 0.8a3.6 3.6 0 0 0-3.6 3.6C2.4 7.2 6 11.2 6 11.2s3.6-4 3.6-6.8A3.6 3.6 0 0 0 6 .8zm0 5a1.4 1.4 0 1 1 0-2.8 1.4 1.4 0 0 1 0 2.8z" fill="currentColor"/></svg>
        482 E Thornbury Avenue Dellhaven, MN 54911
      </li>
      <li>
        <svg viewBox="0 0 12 12" aria-hidden="true"><rect x="2.5" y="1" width="7" height="10" rx="1.3" fill="none" stroke="currentColor" stroke-width="1.2"/><line x1="5" y1="9.3" x2="7" y2="9.3" stroke="currentColor" stroke-width="1"/></svg>
        715-555-0187
      </li>
    </ul>
    <div class="accent-stripe"></div>
  </section>

  <section class="card card--logo" aria-label="Business card, logo side">
    <svg class="corner-swoosh" viewBox="0 0 200 150" preserveAspectRatio="none" aria-hidden="true">
      <path d="M200 0 C170 70 110 125 20 150 L200 150 Z" fill="var(--steel-blue-deep)"/>
    </svg>
    <div class="brand">
      <span class="brand-dot" aria-hidden="true"></span>
      <span class="brand-name">BRENVIK</span>
    </div>
    <p class="tagline">AUTO SALES &amp; SERVICE</p>
  </section>

  <section class="lockup" aria-label="Brenvik logo lockup">
    <div class="brand">
      <span class="brand-dot" aria-hidden="true"></span>
      <span class="brand-name">BRENVIK</span>
    </div>
    <p class="tagline">AUTO SALES &amp; SERVICE</p>
  </section>

</main>
</body>
</html>
```